Orbin Vale Systems

Our company is about IT hardwares and IT solutions. IT hardware such as PC, RAMS, storage and servers. IT solutions such as project management, BA. We are also selling new technology too.

Target Market(s)

Consumer, Small to Medium Business, Corporate

Requirements
Must have
• The business card must have the following:
• Name:
• Title:
• Contact Number:
• Email address:
• Website:
• Color: Must match the logo color upgrade

```html
<!DOCTYPE html>
<html lang="en">
<head>
<meta charset="utf-8">
<title>Orbin Vale Systems — Business Card</title>
<link href="https://fonts.googleapis.com/css2?family=Saira:wght@400;700&family=Michroma&display=swap" rel="stylesheet">
<style>
  :root {
    --backdrop: #d9d9d9;
    --card-white: #f7f7f7;
    --ink-gray: #4d4d4d;
    --band-gray: #585858;
    --orange-light: #e0a350;
    --orange-deep: #c46a28;
    --orange-text: #d98a38;
    --contact-ink: #1e1e1e;
  }
  * { margin: 0; padding: 0; box-sizing: border-box; }
  html, body { width: 1200px; height: 864px; overflow: hidden; }
  body {
    background: var(--backdrop);
    position: relative;
    font-family: "Saira", sans-serif;
  }
  .card {
    position: absolute;
    width: 600px;
    height: 343px;
    box-shadow: 0 10px 28px rgba(0,0,0,0.18);
    overflow: hidden;
  }

  /* Back of card */
  .card-back {
    left: 540px; top: 60px;
    background: linear-gradient(120deg, var(--orange-light) 0%, var(--orange-deep) 100%);
  }
  .card-back .brand {
    position: absolute;
    right: 48px; bottom: 70px;
    text-align: right;
    color: #ffffff;
    font-family: "Saira", sans-serif;
    font-weight: 700;
    line-height: 1;
  }
  .card-back .brand-main { font-size: 50px; letter-spacing: 1px; }
  .card-back .brand-sub { font-size: 22px; letter-spacing: 16px; margin-top: 6px; margin-right: -16px; }

  /* Front of card */
  .card-front {
    left: 60px; top: 440px;
    background: var(--card-white);
  }
  .card-front .bands { position: absolute; left: 0; top: 0; }
  .card-front .brand {
    position: absolute;
    left: 38px; top: 52px;
    width: 250px;
    color: var(--ink-gray);
    font-weight: 700;
    line-height: 1;
    text-align: center;
  }
  .brand-mark {
    display: block;
    width: 22px; height: 22px;
    margin: 0 auto 14px;
    background: var(--orange-text);
  }
  .card-front .brand-main { font-size: 40px; letter-spacing: 0.5px; }
  .card-front .brand-sub { font-size: 18px; letter-spacing: 13px; margin-top: 8px; margin-right: -13px; }
  .divider {
    position: absolute;
    left: 306px; top: 42px;
    width: 2px; height: 170px;
    background: var(--ink-gray);
  }
  .person {
    position: absolute;
    left: 330px; top: 56px;
    font-family: "Michroma", sans-serif;
    line-height: 1.15;
  }
  .person-name { font-size: 17px; color: var(--ink-gray); }
  .person-title { font-size: 14px; color: var(--orange-text); }
  .contacts {
    position: absolute;
    left: 330px; top: 128px;
    list-style: none;
    font-family: "Michroma", sans-serif;
    font-size: 13px;
    color: var(--contact-ink);
  }
  .contact-item { display: flex; align-items: center; gap: 10px; height: 22px; margin-bottom: 3px; }
  .contact-icon { width: 18px; height: 18px; flex: none; }
</style>
</head>
<body>

<section class="card card-back" aria-label="Business card back">
  <div class="brand">
    <div class="brand-main">ORBIN VALE</div>
    <div class="brand-sub">SYSTEMS</div>
  </div>
</section>

<section class="card card-front" aria-label="Business card front">
  <svg class="bands" width="600" height="343" viewBox="0 0 600 343" aria-hidden="true">
    <defs>
      <linearGradient id="orangeBand" x1="0" y1="0" x2="1" y2="0.4">
        <stop offset="0" stop-color="#e0a350"/>
        <stop offset="1" stop-color="#c46a28"/>
      </linearGradient>
    </defs>
    <polygon points="0,212 290,212 240,272 0,272" fill="#585858"/>
    <polygon points="256,272 600,272 600,320 220,320 256,272" fill="url(#orangeBand)"/>
    <polygon points="300,212 600,212 600,260 262,260" fill="none"/>
  </svg>

  <div class="brand">
    <span class="brand-mark" aria-hidden="true"></span>
    <div class="brand-main">ORBIN VALE</div>
    <div class="brand-sub">SYSTEMS</div>
  </div>

  <div class="divider"></div>

  <div class="person">
    <div class="person-name">MARA QUILLON</div>
    <div class="person-title">MANAGER</div>
  </div>

  <ul class="contacts">
    <li class="contact-item">
      <svg class="contact-icon" viewBox="0 0 18 18" aria-hidden="true">
        <rect width="18" height="18" fill="#d98a38"/>
        <path d="M6 4 L8 4 L8.8 7 L7.6 8 Q8.6 10.2 10 11 L11 9.8 L14 10.6 L14 12.6 Q12.5 14.2 10 13 Q5.5 10.5 4.6 6.4 Q4.4 4.8 6 4 Z" fill="#fff"/>
      </svg>
      <span>+1-555-014-2287</span>
    </li>
    <li class="contact-item">
      <svg class="contact-icon" viewBox="0 0 18 18" aria-hidden="true">
        <rect width="18" height="18" fill="#d98a38"/>
        <rect x="3.5" y="5" width="11" height="8" fill="none" stroke="#fff" stroke-width="1.3"/>
        <polyline points="3.5,5 9,9.6 14.5,5" fill="none" stroke="#fff" stroke-width="1.3"/>
      </svg>
      <span>mara@orbinvale.com</span>
    </li>
    <li class="contact-item">
      <svg class="contact-icon" viewBox="0 0 18 18" aria-hidden="true">
        <rect width="18" height="18" fill="#d98a38"/>
        <circle cx="9" cy="9" r="5.5" fill="none" stroke="#fff" stroke-width="1.2"/>
        <ellipse cx="9" cy="9" rx="2.3" ry="5.5" fill="none" stroke="#fff" stroke-width="1"/>
        <line x1="3.5" y1="9" x2="14.5" y2="9" stroke="#fff" stroke-width="1"/>
      </svg>
      <span>www.orbinvale.com</span>
    </li>
  </ul>
</section>

</body>
</html>
```